business card for a massage therapy practice named 'Meadow and Rowan Massage Studio'

I really need a trendy, yet easy on the eyes business card to complement my logo. Ideally with some gold or rose gold foil work.

My uploaded file of the logo I have in horizontal but I have a vertical version as well. Another color that is used in the website is a blush pink here and there. I'd like to see some trendy tropical leaves in the design.

```html
<!DOCTYPE html>
<html lang="en">
<head>
<meta charset="utf-8">
<title>Meadow and Rowan Massage Studio — Business Card</title>
<link href="https://fonts.googleapis.com/css2?family=Roboto:wght@400;500;700&family=Great+Vibes&display=swap" rel="stylesheet">
<style>
  :root {
    --ink: #1d1d1d;
    --text: #333333;
    --gold: #a89068;
    --teal: #7fcfb5;
    --teal-dark: #5cb89c;
    --blush: #f3c8dc;
    --blush-icon: #f2a9c6;
    --rose: #e7a2bd;
    --jungle-dark: #0b201b;
    --jungle-mid: #1f4a3a;
    --paper: #ffffff;
    --stage: #f6f6f4;
  }
  * { box-sizing: border-box; margin: 0; padding: 0; }
  html, body { width: 1200px; height: 1040px; overflow: hidden; }
  body {
    background: var(--stage);
    font-family: "Roboto", Arial, sans-serif;
    color: var(--text);
    position: relative;
  }

  /* Brand mark at the top */
  .brand-mark {
    position: absolute; top: 118px; left: 0; width: 1200px;
    display: flex; justify-content: center; align-items: center; gap: 16px;
  }
  .brand-mark .dot { width: 40px; height: 40px; border-radius: 50%; background: var(--gold); }
  .brand-mark .name {
    font-family: "Roboto", Arial, sans-serif; font-weight: 500;
    font-size: 40px; color: var(--ink); letter-spacing: 0.5px;
  }

  .card {
    position: absolute; width: 424px; height: 248px;
    box-shadow: 0 8px 24px rgba(0,0,0,0.18);
    overflow: hidden;
  }

  /* Front of card */
  .card-front { left: 236px; top: 276px; }
  .card-front .leaf-art {
    position: absolute; inset: 0;
    background:
      radial-gradient(ellipse at 50% 50%, var(--jungle-dark) 38%, transparent 70%),
      linear-gradient(135deg, var(--jungle-mid) 0%, #3b5a38 25%, var(--jungle-dark) 50%, #4a2a30 78%, var(--jungle-mid) 100%);
  }
  .card-front .front-name {
    position: absolute; top: 96px; left: 0; width: 100%;
    display: flex; justify-content: center; align-items: center; gap: 10px;
  }
  .card-front .front-name .dot { width: 22px; height: 22px; border-radius: 50%; background: var(--rose); }
  .card-front .front-name .name {
    font-weight: 500; font-size: 20px; color: var(--rose);
  }
  .card-front .handle {
    position: absolute; bottom: 22px; width: 100%; text-align: center;
    color: #f1f1f1; font-size: 12px;
  }

  /* Back of card */
  .card-back { left: 447px; top: 554px; background: var(--paper); }
  .card-back .holder {
    position: absolute; top: 19px; right: 18px; text-align: right; line-height: 1.3;
  }
  .card-back .holder .person { font-weight: 700; font-size: 13px; color: var(--ink); }
  .card-back .holder .tel { font-size: 12.5px; color: var(--ink); }

  .sessions { position: absolute; top: 66px; left: 16px; right: 16px; }
  .sessions h2 {
    font-family: "Great Vibes", cursive; font-weight: 400;
    font-size: 19px; color: var(--teal-dark); margin-bottom: 3px;
  }
  .sessions ul {
    list-style: none; display: grid; grid-template-columns: 194px 1fr;
    grid-auto-flow: column; grid-template-rows: repeat(3, 16.5px);
    font-size: 11.5px; color: var(--text);
  }
  .sessions li { display: flex; align-items: center; gap: 6px; }
  .sessions li svg { flex: none; }

  .contact-band {
    position: absolute; left: 0; bottom: 0; width: 100%; height: 97px;
    background: var(--blush);
  }
  .contact-list {
    position: absolute; left: 18px; top: 17px; list-style: none;
    font-size: 13px; color: var(--ink); line-height: 19.5px;
  }
  .contact-list li { display: flex; align-items: center; gap: 8px; }
  .contact-list svg { width: 14px; height: 14px; flex: none; }

  .call-box {
    position: absolute; right: 18px; top: 14px; width: 142px;
    border: 2px solid var(--teal); background: var(--paper);
  }
  .call-box .label {
    font-weight: 500; font-size: 12.5px; color: var(--ink); padding: 7px 10px 6px;
  }
  .call-box .number {
    background: var(--teal); color: var(--ink); font-weight: 700; font-size: 14px;
    padding: 6px 8px 7px; display: flex; align-items: center; gap: 6px;
  }
</style>
</head>
<body>

  <header class="brand-mark">
    <span class="dot"></span>
    <span class="name">Meadow &amp; Rowan Massage Studio</span>
  </header>

  <section class="card card-front">
    <div class="leaf-art" role="img" aria-label="Tropical palm leaves, lilies and red bromeliads framing a dark green card"></div>
    <div class="front-name">
      <span class="dot"></span>
      <span class="name">Meadow &amp; Rowan Massage Studio</span>
    </div>
    <div class="handle">@meadowandrowan</div>
  </section>

  <section class="card card-back">
    <div class="holder">
      <div class="person">Dana Whitfield LMT</div>
      <div class="tel">916.555.0148</div>
    </div>

    <div class="sessions">
      <h2>Our Most Popular Sessions</h2>
      <ul>
        <li><svg width="11" height="7" viewBox="0 0 11 7"><ellipse cx="5.5" cy="3.5" rx="5.2" ry="2.6" transform="rotate(-20 5.5 3.5)" fill="var(--blush-icon)"/></svg>Clinical Bodywork</li>
        <li><svg width="11" height="7" viewBox="0 0 11 7"><ellipse cx="5.5" cy="3.5" rx="5.2" ry="2.6" transform="rotate(-20 5.5 3.5)" fill="var(--blush-icon)"/></svg>Therapeutic Massage</li>
        <li><svg width="11" height="7" viewBox="0 0 11 7"><ellipse cx="5.5" cy="3.5" rx="5.2" ry="2.6" transform="rotate(-20 5.5 3.5)" fill="var(--blush-icon)"/></svg>Integrated Hot Stone Massage</li>
        <li><svg width="11" height="7" viewBox="0 0 11 7"><ellipse cx="5.5" cy="3.5" rx="5.2" ry="2.6" transform="rotate(-20 5.5 3.5)" fill="var(--blush-icon)"/></svg>Lymphatic Drainage Massage</li>
        <li><svg width="11" height="7" viewBox="0 0 11 7"><ellipse cx="5.5" cy="3.5" rx="5.2" ry="2.6" transform="rotate(-20 5.5 3.5)" fill="var(--blush-icon)"/></svg>Sacramento Sinus Facial</li>
        <li><svg width="11" height="7" viewBox="0 0 11 7"><ellipse cx="5.5" cy="3.5" rx="5.2" ry="2.6" transform="rotate(-20 5.5 3.5)" fill="var(--blush-icon)"/></svg>Australian Foot Treatment</li>
      </ul>
    </div>

    <div class="contact-band">
      <ul class="contact-list">
        <li>
          <svg viewBox="0 0 14 14"><rect x="1" y="3" width="12" height="8.5" fill="var(--ink)"/><path d="M1 3.5 L7 8 L13 3.5" stroke="var(--blush)" stroke-width="1.2" fill="none"/></svg>
          hello@meadowandrowan.com
        </li>
        <li>
          <svg viewBox="0 0 14 14"><rect x="2.5" y="3" width="9" height="6.5" fill="none" stroke="var(--ink)" stroke-width="1.3"/><rect x="0.5" y="10" width="13" height="1.6" fill="var(--ink)"/></svg>
          www.meadowandrowan.com
        </li>
        <li>@meadowandrowan</li>
      </ul>

      <div class="call-box">
        <div class="label">Call for Appointment</div>
        <div class="number">
          <svg width="12" height="12" viewBox="0 0 12 12"><path d="M2.5 1 L4.5 1 L5.2 3.6 L4 4.6 C4.6 6 5.8 7.2 7.2 7.8 L8.2 6.6 L11 7.3 L11 9.4 C11 10.2 10.3 10.8 9.5 10.7 C5 10.2 1.6 6.8 1.1 2.4 C1 1.6 1.7 1 2.5 1 Z" fill="var(--ink)"/></svg>
          (916) 555-0148
        </div>
      </div>
    </div>
  </section>

</body>
</html>
```